Quiet Harbor Podcast Business Card Design

Needing a business card with the logo design provided for Quiet Harbor Podcast. I am looking for a modern style that fits the current logo.

Info:
Name: Teodor Vask
Title: Creator/Host
Email: teodor@quietharborcast.com
Phone: (555) 274-9163
www.quietharborcast.com
Twitter: @qharborcast
Instagram: @quietharborcastshow
Facebook: Quiet Harbor Podcast

Industry/Entity Type

Business

Font styles to use
Sans Serif

Colors
000000
ffffff

Requirements
Must have
• modern, clean design
Nice to have
• social media contact info

```html
<!DOCTYPE html>
<html lang="en">
<head>
<meta charset="utf-8">
<title>Quiet Harbor Podcast – Business Card</title>
<link rel="stylesheet" href="https://fonts.googleapis.com/css2?family=Roboto:wght@400;500;700&family=Roboto+Condensed:wght@500;700&display=swap">
<style>
  :root {
    --backdrop: #d9d9d9;
    --card-light: #f4f4f4;
    --card-dark: #1a1a1a;
    --ink: #333333;
    --ink-soft: #4a4a4a;
    --band-dark: #2e2e2e;
    --band-grey: #6a6a6a;
    --rule: #9a9a9a;
    --white: #ffffff;
  }
  html, body {
    margin: 0;
    padding: 0;
    width: 1200px;
    height: 960px;
    overflow: hidden;
    background: var(--backdrop);
  }
  .canvas {
    position: relative;
    width: 1200px;
    height: 960px;
  }
  .card {
    position: absolute;
    left: 312px;
    width: 600px;
    height: 343px;
    box-shadow: 0 2px 6px rgba(0,0,0,0.25);
    overflow: hidden;
  }
  .card--front { top: 113px; background: var(--card-light); }
  .card--back  { top: 472px; background: var(--card-dark); }

  .brand {
    position: absolute;
    text-align: center;
    font-family: "Roboto", sans-serif;
    font-weight: 500;
  }
  .brand__mark {
    display: block;
    margin: 0 auto 14px;
    width: 48px;
    height: 48px;
  }
  .brand__name {
    display: block;
    text-transform: uppercase;
    letter-spacing: 0.5px;
    line-height: 1;
  }
  .brand__sub {
    display: block;
    text-transform: uppercase;
    line-height: 1;
  }
  .card--front .brand {
    left: 30px;
    width: 240px;
    top: 118px;
    color: var(--ink);
  }
  .card--front .brand__mark { background: var(--ink); }
  .card--front .brand__name { font-size: 22px; }
  .card--front .brand__sub { font-size: 9px; letter-spacing: 5px; margin-top: 4px; }

  .card--back .brand {
    left: 0;
    width: 600px;
    top: 98px;
    color: var(--white);
  }
  .card--back .brand__mark { background: var(--white); width: 60px; height: 60px; margin-bottom: 24px; }
  .card--back .brand__name { font-size: 28px; }
  .card--back .brand__sub { font-size: 11px; letter-spacing: 6px; margin-top: 5px; }

  .divider {
    position: absolute;
    left: 286px;
    top: 86px;
    width: 1px;
    height: 176px;
    background: var(--rule);
  }
  .contact {
    position: absolute;
    left: 310px;
    top: 84px;
    color: var(--ink);
  }
  .contact__name {
    margin: 0;
    font-family: "Roboto Condensed", sans-serif;
    font-weight: 700;
    font-size: 21px;
    line-height: 1;
    text-transform: uppercase;
  }
  .contact__title {
    margin: 5px 0 18px;
    font-family: "Roboto Condensed", sans-serif;
    font-weight: 500;
    font-size: 15px;
    color: var(--ink-soft);
    text-transform: uppercase;
  }
  .contact__list {
    list-style: none;
    margin: 0;
    padding: 0;
    font-family: "Roboto", sans-serif;
    font-size: 14px;
    color: var(--ink-soft);
  }
  .contact__item {
    display: flex;
    align-items: center;
    height: 19px;
  }
  .contact__icon {
    width: 12px;
    height: 12px;
    margin-right: 12px;
    flex: none;
    fill: var(--ink);
  }
  .contact__dot {
    width: 9px;
    height: 9px;
    margin: 0 14px 0 2px;
    flex: none;
    background: var(--ink);
    border-radius: 50%;
  }
  .band {
    position: absolute;
    left: 0;
    bottom: 0;
    width: 600px;
    height: 18px;
  }
</style>
</head>
<body>
<main class="canvas">

  <section class="card card--front" aria-label="Card front">
    <div class="brand">
      <span class="brand__mark"></span>
      <span class="brand__name">Quiet Harbor</span>
      <span class="brand__sub">Podcast</span>
    </div>

    <div class="divider"></div>

    <div class="contact">
      <h1 class="contact__name">Teodor Vask</h1>
      <p class="contact__title">Creator/Host</p>
      <ul class="contact__list">
        <li class="contact__item">
          <svg class="contact__icon" viewBox="0 0 12 12" aria-hidden="true"><path d="M2.4 0.8 4.3 2.7 3.3 4.2c.8 1.7 2.1 3 3.8 3.8l1.5-1 1.9 1.9-1.4 1.9C5 10.6 1.4 7 1.2 2.2z"/></svg>
          (555) 274-9163
        </li>
        <li class="contact__item">
          <svg class="contact__icon" viewBox="0 0 12 12" aria-hidden="true"><path d="M1 3h10v7H1z M1.5 3.5 6 7l4.5-3.5" fill="none" stroke="#333" stroke-width="1.2"/></svg>
          teodor@quietharborcast.com
        </li>
        <li class="contact__item">
          <svg class="contact__icon" viewBox="0 0 12 12" aria-hidden="true"><circle cx="6" cy="6" r="5" fill="none" stroke="#333" stroke-width="1.2"/><path d="M1 6h10M6 1c-2.5 3-2.5 7 0 10M6 1c2.5 3 2.5 7 0 10" fill="none" stroke="#333" stroke-width="1"/></svg>
          www.quietharborcast.com
        </li>
        <li class="contact__item"><span class="contact__dot"></span>Quiet Harbor Podcast</li>
        <li class="contact__item"><span class="contact__dot"></span>@quietharborcastshow</li>
        <li class="contact__item"><span class="contact__dot"></span>@qharborcast</li>
      </ul>
    </div>

    <svg class="band" viewBox="0 0 600 18" aria-hidden="true">
      <rect x="0" y="0" width="340" height="18" fill="var(--band-dark)"/>
      <polygon points="346,18 352,0 600,0 600,18" fill="var(--band-grey)"/>
      <polygon points="337,18 343,0 346,0 340,18" fill="var(--white)"/>
    </svg>
  </section>

  <section class="card card--back" aria-label="Card back">
    <div class="brand">
      <span class="brand__mark"></span>
      <span class="brand__name">Quiet Harbor</span>
      <span class="brand__sub">Podcast</span>
    </div>
  </section>

</main>
</body>
</html>
```